Looking to design a new sign for our church.

Looking for a new sign
4 x 8 feet dimension
We are renaming the church "Medlow Ridge Community Church"
looking for legible graphics
Would like some type of backdrop being a family tree (oak) / open to other ideas as you are led
I have included a pic of the old sign for your review
would like to incorporate our ministry logo on the lower right hand corner of the sign / see file attached

```html
<!DOCTYPE html>
<html lang="en">
<head>
<meta charset="utf-8">
<title>Medlow Ridge Community Church – Sign Options</title>
<link rel="stylesheet" href="https://fonts.googleapis.com/css2?family=Marcellus&family=Work+Sans:wght@600&display=swap">
<style>
  :root {
    --backdrop: #bebebe;
    --paper: #ffffff;
    --black: #000000;
    --black-soft: #3b3b3b;
    --maroon: #681d27;
    --maroon-soft: #8e4b54;
  }
  html, body {
    margin: 0;
    padding: 0;
    width: 1200px;
    height: 1200px;
    overflow: hidden;
    background: var(--backdrop);
  }
  .canvas {
    position: relative;
    width: 1200px;
    height: 1200px;
  }
  .sign {
    position: absolute;
    left: 120px;
    width: 960px;
    height: 480px;
    display: block;
  }
  .sign--black { top: 70px; --accent: var(--black); --emblem-tone: var(--black-soft); }
  .sign--maroon { top: 654px; --accent: var(--maroon); --emblem-tone: var(--maroon-soft); }

  .sign__base { fill: var(--paper); }
  .sign__band { fill: var(--accent); }
  .sign__frame { fill: none; stroke: var(--paper); stroke-width: 8; }
  .sign__emblem { fill: var(--emblem-tone); }

  .sign__name {
    font-family: "Marcellus", serif;
    fill: var(--paper);
  }
  .sign__name--main { font-size: 112px; }
  .sign__name--sub { font-size: 83px; }

  .sign__schedule {
    font-family: "Work Sans", sans-serif;
    font-weight: 600;
    font-size: 47px;
    fill: var(--accent);
  }
  .ministry__name {
    font-family: "Work Sans", sans-serif;
    font-weight: 600;
    font-size: 18px;
    fill: var(--accent);
  }
  .ministry__dot { fill: none; stroke: var(--accent); stroke-width: 3; }
</style>
</head>
<body>
<main class="canvas">

  <svg class="sign sign--black" viewBox="0 0 1546 773" role="group" aria-label="Sign option in black">
    <rect class="sign__base" x="0" y="0" width="1546" height="773"/>
    <rect class="sign__band" x="0" y="0" width="1546" height="506"/>
    <rect class="sign__frame" x="34" y="30" width="1486" height="446"/>
    <rect class="sign__emblem" x="110" y="62" width="352" height="444" role="img" aria-label="Church emblem: cross above a church roof"/>
    <text class="sign__name sign__name--main" x="1444" y="259" text-anchor="end">MEDLOW RIDGE</text>
    <text class="sign__name sign__name--sub" x="1446" y="364" text-anchor="end">COMMUNITY CHURCH</text>
    <text class="sign__schedule" x="110" y="625">Worship Service (10:30 AM), Sunday School (9:30 AM)</text>
    <text class="sign__schedule" x="110" y="692">Wednesday Service (6:00 PM)</text>
    <text class="ministry__name" x="1432" y="560" text-anchor="middle">Harvest</text>
    <text class="ministry__name" x="1432" y="583" text-anchor="middle">Path</text>
    <text class="ministry__name" x="1432" y="606" text-anchor="middle">Ministries</text>
    <circle class="ministry__dot" cx="1432" cy="690" r="28"/>
  </svg>

  <svg class="sign sign--maroon" viewBox="0 0 1546 773" role="group" aria-label="Sign option in maroon">
    <rect class="sign__base" x="0" y="0" width="1546" height="773"/>
    <rect class="sign__band" x="0" y="0" width="1546" height="506"/>
    <rect class="sign__frame" x="32" y="32" width="1484" height="444"/>
    <rect class="sign__emblem" x="106" y="62" width="352" height="444" role="img" aria-label="Church emblem: cross above a church roof"/>
    <text class="sign__name sign__name--main" x="1440" y="262" text-anchor="end">MEDLOW RIDGE</text>
    <text class="sign__name sign__name--sub" x="1442" y="370" text-anchor="end">COMMUNITY CHURCH</text>
    <text class="sign__schedule" x="106" y="625">Worship Service (10:30 AM), Sunday School (9:30 AM)</text>
    <text class="sign__schedule" x="106" y="692">Wednesday Service (6:00 PM)</text>
    <text class="ministry__name" x="1428" y="560" text-anchor="middle">Harvest</text>
    <text class="ministry__name" x="1428" y="583" text-anchor="middle">Path</text>
    <text class="ministry__name" x="1428" y="606" text-anchor="middle">Ministries</text>
    <circle class="ministry__dot" cx="1428" cy="690" r="28"/>
  </svg>

</main>
</body>
</html>
```